Preferred pricing vendor

We are a plumbing company that has many services
-Boilers & Controls
-Plumbing & Heating
-HVAC & Refrigeration
-Preventative Maintenacne
-Gas fitting & Drain Cleaning

We primarily look after condo buildings, and our preferred service rates ($98, $93, or $88 depending on the contract) extend to all of our clients. So in essence, we look after the mechanical room and common equipment but our clients can call us in for drain cleaning or replacing a fixture in their suite. The discounted rates apply to the personal residence. We want a flyer to let them know they get a discount on our services. A one-pager we can send out to all of our contract clients.

Included source files for our letterhead and logo just so you can see the colours we go with.

Target Market(s)

Residential repairs, individual people, replacement of fixtures in-suite specific repairs

Requirements
Must have
• be colourful and attractive

```html
<!DOCTYPE html>
<html lang="en">
<head>
<meta charset="utf-8">
<title>Keystone Mechanical – Preferred Rates Flyer</title>
<link href="https://fonts.googleapis.com/css2?family=Anton&family=Roboto:wght@400;700;900&display=swap" rel="stylesheet">
<style>
:root{
  --blue:#245a96;
  --blue-bright:#2a6fc0;
  --navy:#1b3a5e;
  --orange:#ef5a24;
  --grey:#6e6e6e;
  --row:#ececec;
  --page:#ffffff;
  --backdrop:#f2f2f2;
}
*{margin:0;padding:0;box-sizing:border-box}
html,body{width:1200px;height:2597px;overflow:hidden;background:var(--backdrop)}
.flyer{position:absolute;left:0;top:523px;width:734px;height:950px;background:var(--page);
  transform:scale(1.6349);transform-origin:0 0;overflow:hidden;font-family:'Roboto',sans-serif;
  box-shadow:0 2px 6px rgba(0,0,0,.25)}
.abs{position:absolute}
.brand{left:62px;top:62px;display:flex;align-items:center;gap:8px;color:var(--blue-bright);
  font-weight:900;font-size:19px;letter-spacing:.5px}
.brand-dot{width:14px;height:14px;border-radius:50%;background:var(--orange)}
.hero-band{left:0;top:0}
.hero-accent{left:370px;top:-45px;width:400px;height:390px;border-radius:50%;
  background:radial-gradient(circle at 50% 50%,#f26a35,var(--orange))}
.headline{left:45px;top:124px;color:#fff;font-family:'Anton',sans-serif;line-height:1}
.headline .l1{font-size:58px;display:block;letter-spacing:.5px}
.headline .l2{font-size:58px;display:block;margin-top:-2px}
.headline .l3{font-size:30px;display:block;margin-top:4px;letter-spacing:.3px}
.photo{background:linear-gradient(135deg,#8fa0ad,#4b4f55 60%,#2f3236)}
.photo-hero{left:413px;top:-10px;width:320px;height:320px;border-radius:50%}
.photo-feature{left:47px;top:338px;width:288px;height:157px;border-radius:22px 4px 22px 4px}
.intro{left:47px;top:519px;width:300px;font-size:12.2px;font-weight:700;color:#333;line-height:1.2}
.contract{left:50px;top:673px;font-size:16px;font-weight:700;letter-spacing:1.4px;color:var(--grey)}
.services{left:373px;top:340px;width:312px}
.services-head{height:53px;background:var(--grey);border-radius:0 30px 0 0;color:#fff;
  font-size:29px;font-weight:700;padding:12px 0 0 41px;letter-spacing:.5px}
.service{position:relative;height:55px;background:linear-gradient(#fff,var(--row));border-bottom:2px solid #d9d9d9;
  display:flex;align-items:center;padding-left:79px;font-size:12.2px;font-weight:700;color:var(--blue-bright);letter-spacing:.4px}
.service:last-child{border-radius:0 0 40px 0}
.service-icon{position:absolute;left:0;top:0;width:47px;height:100%;background:var(--orange);display:flex;align-items:center;justify-content:center}
.note{left:81px;top:707px;width:564px;height:36px;border-radius:18px;background:var(--grey);color:#fff;
  font-size:19px;font-weight:700;text-align:center;line-height:36px}
.gallery{top:748px;width:208px;height:109px;border-radius:4px}
.g1{left:47px;background:linear-gradient(90deg,#dfe3e6,#a9afb4)}
.g2{left:262px;background:linear-gradient(90deg,#bfc4c8,#8a9096)}
.g3{left:477px;background:linear-gradient(90deg,#3e4a4c,#7b8a86)}
.phones{left:50px;top:878px;width:379px;height:42px;border-radius:21px;
  background:linear-gradient(90deg,var(--blue-bright) 0 49%,var(--grey) 49% 100%);
  color:#fff;font-size:17px;font-weight:700;letter-spacing:.6px;display:flex;align-items:center}
.phones .p1{margin-left:14px}
.phones .p2{margin-left:auto;margin-right:26px}
.phone-icon{position:absolute;left:171px;top:6px;width:30px;height:30px;border-radius:50%;background:#fff}
.contact{left:441px;top:878px;font-size:14.5px;color:#222;line-height:24px}
.contact-row{display:flex;align-items:center;gap:12px}
</style>
</head>
<body>
<div class="flyer">

  <div class="abs hero-accent" role="img" aria-label="Decorative orange backdrop behind the hero photo"></div>

  <svg class="abs hero-band" width="734" height="330" viewBox="0 0 734 330">
    <polygon points="0,110 385,110 385,295 0,295" fill="var(--blue)"/>
    <polygon points="50,295 420,295 430,307 60,307" fill="var(--orange)"/>
  </svg>
  <div class="abs photo photo-hero" role="img" aria-label="Technician in hard hat working on mechanical equipment"></div>

  <div class="abs brand"><span class="brand-dot"></span>KEYSTONE MECHANICAL INC</div>

  <h1 class="abs headline"><span class="l1">AFFORDABLE</span><span class="l2">MECHANICAL</span><span class="l3">SYSTEM MAINTENANCE</span></h1>

  <div class="abs photo photo-feature" role="img" aria-label="Technician adjusting pipework"></div>
  <p class="abs intro">We primarily look after condo buildings, and our preferred service rates</p>

  <svg class="abs" style="left:47px;top:555px" width="304" height="112" viewBox="0 0 304 112">
    <g font-family="Anton, sans-serif" text-anchor="middle">
      <polygon points="0,70 98,70 98,110 0,110" fill="var(--orange)"/>
      <polygon points="103,70 201,70 201,110 103,110" fill="var(--navy)"/>
      <polygon points="206,70 304,70 304,110 206,110" fill="var(--blue-bright)"/>
      <polygon points="0,70 49,95 98,70" fill="#fff" opacity=".35"/>
      <polygon points="103,70 152,95 201,70" fill="#fff" opacity=".35"/>
      <polygon points="206,70 255,95 304,70" fill="#fff" opacity=".35"/>
      <g>
        <circle cx="48" cy="45" r="37" fill="#fff" stroke="var(--orange)" stroke-width="7"/>
        <text x="51" y="58" font-size="34" fill="var(--blue)">98</text><text x="30" y="38" font-size="12" fill="var(--blue)">$</text>
      </g>
      <g>
        <circle cx="152" cy="45" r="37" fill="#fff" stroke="var(--orange)" stroke-width="7"/>
        <text x="155" y="58" font-size="34" fill="var(--blue)">93</text><text x="134" y="38" font-size="12" fill="var(--blue)">$</text>
      </g>
      <g>
        <circle cx="254" cy="45" r="37" fill="#fff" stroke="var(--orange)" stroke-width="7"/>
        <text x="257" y="58" font-size="34" fill="var(--blue)">88</text><text x="236" y="38" font-size="12" fill="var(--blue)">$</text>
      </g>
    </g>
  </svg>
  <p class="abs contract">DEPENDING ON THE CONTRACT</p>

  <section class="abs services">
    <h2 class="services-head">OUR SERVICES</h2>
    <div class="service"><span class="service-icon"><svg width="26" height="26"><circle cx="13" cy="13" r="10" fill="none" stroke="#fff" stroke-width="2.5"/></svg></span>BOILERS &amp; CONTROLS</div>
    <div class="service"><span class="service-icon"><svg width="26" height="26"><circle cx="13" cy="13" r="10" fill="none" stroke="#fff" stroke-width="2.5"/><path d="M13 7c3 4 4 6 0 11c-4-5-3-7 0-11z" fill="#fff"/></svg></span>PLUMBING &amp; HEATING</div>
    <div class="service"><span class="service-icon"><svg width="26" height="26"><circle cx="13" cy="13" r="10" fill="none" stroke="#fff" stroke-width="2.5"/><path d="M8 13h10M13 8v10" stroke="#fff" stroke-width="2.5"/></svg></span>HVAC &amp; REFRIGERATION</div>
    <div class="service"><span class="service-icon"><svg width="26" height="26"><circle cx="13" cy="13" r="10" fill="none" stroke="#fff" stroke-width="2.5"/><path d="M9 17v-7M13 17v-8M17 17v-7" stroke="#fff" stroke-width="2"/></svg></span>PREVENTATIVE MAINTENACNE</div>
    <div class="service"><span class="service-icon"><svg width="26" height="26"><circle cx="13" cy="13" r="10" fill="none" stroke="#fff" stroke-width="2.5"/><path d="M8 16h10M10 16v-5M16 16v-5" stroke="#fff" stroke-width="2"/></svg></span>GAS FITTING &amp; DRAIN CLEANING</div>
  </section>

  <p class="abs note">The discounted rates apply to the personal residence.</p>

  <div class="abs gallery g1" role="img" aria-label="Row of electrical control cabinets"></div>
  <div class="abs gallery g2" role="img" aria-label="Boiler room with expansion tanks"></div>
  <div class="abs gallery g3" role="img" aria-label="Mechanical room pipes and pumps"></div>

  <div class="abs phones">
    <span class="p1">(403) 555-0148</span>
    <span class="phone-icon"><svg width="30" height="30" viewBox="0 0 30 30"><path d="M10 8l3 0 1.5 4-2 1.5c1 2.5 2.5 4 5 5l1.5-2 4 1.5 0 3c-7 1-14-6-13-13z" fill="var(--navy)"/></svg></span>
    <span class="p2">(780) 555-0172</span>
  </div>

  <div class="abs contact">
    <div class="contact-row"><svg width="22" height="18"><rect x="1" y="2" width="20" height="14" rx="2" fill="none" stroke="var(--blue-bright)" stroke-width="2"/><path d="M1 3l10 7 10-7" fill="none" stroke="var(--blue-bright)" stroke-width="2"/></svg>info@keystonemech.ca</div>
    <div class="contact-row"><svg width="22" height="20"><circle cx="11" cy="10" r="9" fill="none" stroke="var(--blue-bright)" stroke-width="2"/><path d="M2 10h18M11 1c-5 5-5 13 0 18M11 1c5 5 5 13 0 18" fill="none" stroke="var(--blue-bright)" stroke-width="1.5"/></svg>keystonemech.ca</div>
  </div>

</div>
</body>
</html>
```